Business card Zottelgarten

Business card is for a self-employed dog trainer with own dog school. Name and logo of the dog school are available. Color specifications as well. The design should be classy and minimalist, but also modern. An already existing idea would be: Front: Only the logo Back: Contact data

Font styles to use
Serif
Sans Serif
Other font styles liked:
• Trajan Pro

Colors
f78f20

Requirements
Must have
• Name: Margit Wendler-Rasch Title: Dipl. Dog Trainer Contain my logo Follow my font and color preferences (see files)

```html
<!DOCTYPE html>
<html lang="de">
<head>
<meta charset="utf-8">
<title>Zottelgarten – Visitenkarte</title>
<link rel="stylesheet" href="https://fonts.googleapis.com/css2?family=Cinzel:wght@400;700&family=Marcellus&display=swap">
<style>
  :root {
    --backdrop: #4a4a4a;
    --kraft: #b09878;
    --ink: #1a1612;
    --accent: #f78f20;
  }
  * { margin: 0; padding: 0; box-sizing: border-box; }
  html, body { width: 1200px; height: 1000px; overflow: hidden; }
  body { background: var(--backdrop); position: relative; }

  .card {
    position: absolute;
    left: 270px;
    width: 660px;
    height: 378px;
    background: var(--kraft);
    box-shadow: 0 2px 10px rgba(0,0,0,.45);
    color: var(--ink);
  }
  .card--front { top: 108px; }
  .card--back { top: 521px; }

  .brand-dot {
    position: absolute;
    left: 231px; top: 58px;
    width: 196px; height: 196px;
    border-radius: 50%;
    background: var(--ink);
  }
  .brand-name {
    position: absolute;
    left: 0; right: 0; top: 262px;
    text-align: center;
    font-family: "Cinzel", serif;
    font-weight: 400;
    font-size: 44px;
    letter-spacing: 2px;
    line-height: 1;
  }
  .brand-url {
    position: absolute;
    left: 0; right: 0; top: 310px;
    text-align: center;
    font-family: "Cinzel", serif;
    font-weight: 700;
    font-size: 12px;
    letter-spacing: 7px;
    line-height: 1;
  }

  .contact {
    position: absolute;
    left: 38px; top: 214px;
    font-family: "Marcellus", serif;
    text-transform: uppercase;
  }
  .contact__name {
    font-family: "Cinzel", serif;
    font-weight: 700;
    font-size: 22px;
    letter-spacing: .5px;
    line-height: 1.2;
    color: var(--ink);
  }
  .contact__role {
    font-size: 15px;
    margin-top: 2px;
    margin-bottom: 24px;
    color: var(--accent);
  }
  .contact__line {
    font-size: 15px;
    line-height: 23px;
  }
</style>
</head>
<body>
  <section class="card card--front">
    <div class="brand-dot"></div>
    <div class="brand-name">ZOTTELGARTEN</div>
    <div class="brand-url">WWW.ZOTTELGARTEN.CH</div>
  </section>

  <section class="card card--back">
    <div class="contact">
      <div class="contact__name">Margit Wendler-Rasch</div>
      <div class="contact__role">Dipl. Dog Trainer</div>
      <div class="contact__line">0987 654 321</div>
      <div class="contact__line">info@zottelgarten.ch</div>
      <div class="contact__line">www.zottelgarten.ch</div>
    </div>
  </section>
</body>
</html>
```